New Website for World Wide Charity (VELORA)

We need a dynamic web design for our brand new charity organisation that will be working worldwide. We will be funded by donations so need to attract people to donate.

What We Do
We work to optimise the wellbeing of the planet, the animals and all that live within. Our slogan is Achieving Vibrational Equilibrium.

We have included a Powerpoint document which may help you understand what we need, it is just an idea for structure and style, it is not set in stone so feel free to be as creative as you like!
Updates

Designs look the same

Target Market(s)

Adults 18+ with an interest in animal, environmental. Businesses that may like to support our natural world or already support our natural world.

Number of Pages Required

3 page

Colors

Designer to choose colors to be used in the design.

Requirements
Must have
• We need the website to be easy to use and understand.

Web pages will be Home, What We Do, Who We Are, Success Stories, What You Can Do (Blog section), Seek Help, Donate, Join.
Nice to have
• Natural feel, easy to navigate, Ideally the website will look natural and organic.

Natural colours, blues, greens, sand, gold, brown, grey, silver, Orange and yellow for impact.
Should not have
• Should not have a dark coloured theme.

```html
<!DOCTYPE html>
<html lang="en">
<head>
<meta charset="utf-8">
<title>Velora – Help Raise World Fibration</title>
<link href="https://fonts.googleapis.com/css2?family=Poppins:wght@300;400;500;600;700&family=Open+Sans:wght@400;600&display=swap" rel="stylesheet">
<style>
  :root{
    --green:#1f8a3f;
    --green-dark:#17702f;
    --ink:#2a2f33;
    --muted:#7b8186;
    --line:#e3e6e8;
    --white:#ffffff;
    --paper:#f7f8f7;
    --wheat-light:#e4e5df;
    --wheat:#c9a466;
    --wheat-deep:#8c6a3a;
  }
  *{box-sizing:border-box;margin:0;padding:0}
  html,body{width:1200px;height:2196px;overflow:hidden;background:var(--white)}
  body{position:relative;font-family:"Open Sans",Arial,sans-serif;color:var(--ink)}
  .abs{position:absolute}

  /* Header */
  .site-header{position:absolute;top:0;left:0;width:1200px;height:80px;z-index:3}
  .brand{position:absolute;left:44px;top:22px;display:flex;align-items:center;gap:10px;
    font-family:"Poppins",sans-serif;font-weight:600;font-size:16px;color:var(--ink);letter-spacing:1px}
  .brand-dot{width:30px;height:30px;border-radius:50%;background:var(--green)}
  .main-nav{position:absolute;right:56px;top:34px;display:flex;gap:34px;
    font-family:"Poppins",sans-serif;font-size:12px;color:var(--ink)}
  .main-nav a{color:inherit;text-decoration:none;padding-bottom:6px}
  .main-nav a.active{color:var(--green);border-bottom:2px solid var(--green)}

  /* Hero */
  .hero{position:absolute;top:0;left:0;width:1200px;height:600px;
    background:linear-gradient(180deg,#eef0ee 0%,var(--wheat-light) 22%,#d8c396 45%,var(--wheat) 68%,var(--wheat-deep) 100%)}
  .hero-title{position:absolute;left:62px;top:176px;font-family:"Poppins",sans-serif;color:var(--ink);line-height:1.15}
  .hero-title .strong{display:block;font-weight:700;font-size:54px}
  .hero-title .light{display:block;font-weight:300;font-size:52px}
  .hero-text{position:absolute;left:64px;top:318px;width:430px;font-size:12px;line-height:1.7;color:#3b3f42}
  .btn{display:inline-block;font-family:"Poppins",sans-serif;font-size:11px;text-decoration:none}
  .btn-solid{background:var(--green);color:var(--white);padding:11px 22px;border-radius:2px}
  .btn-outline{border:1px solid #cfd3d6;color:var(--ink);padding:9px 20px;background:var(--white)}
  .hero-cta{position:absolute;left:64px;top:438px}

  /* Cards */
  .card{position:absolute;top:600px;width:336px;height:480px;background:var(--white);
    box-shadow:0 6px 20px rgba(0,0,0,.08);text-align:center}
  .card-media{height:220px}
  .card-icon{width:64px;height:64px;border-radius:50%;background:var(--white);margin:-32px auto 0;
    box-shadow:0 3px 10px rgba(0,0,0,.1);display:flex;align-items:center;justify-content:center;position:relative}
  .card-title{font-family:"Poppins",sans-serif;font-weight:500;font-size:22px;margin-top:20px}
  .card-text{width:260px;margin:12px auto 0;font-size:11px;line-height:1.7;color:var(--muted)}
  .card .btn-outline{margin-top:22px}
  .media-forest{background:linear-gradient(160deg,#dfe6e6 0%,#7f918b 40%,#3f5148 100%)}
  .media-snow{background:linear-gradient(180deg,#e9eceb 0%,#b9c2be 50%,#6e7a72 100%)}
  .media-meadow{background:linear-gradient(160deg,#8fae4c 0%,#4f7a2e 55%,#c9b39a 100%)}

  /* Feature rows */
  .feature-title{position:absolute;font-family:"Poppins",sans-serif;font-weight:600;font-size:30px;color:var(--ink)}
  .feature-text{position:absolute;width:470px;font-size:11.5px;line-height:1.75;color:var(--muted)}
  .feature-media{position:absolute;box-shadow:0 6px 20px rgba(0,0,0,.08)}
  .media-road{background:linear-gradient(90deg,#2f4236 0%,#5f7467 40%,#c7cfcb 50%,#5f7467 60%,#2f4236 100%)}
  .media-mist{background:linear-gradient(180deg,#eef0ef 0%,#c4cac6 45%,#7d8780 80%,#5b655e 100%)}

  /* Footer */
  .site-footer{position:absolute;top:1972px;left:0;width:1200px;height:224px;
    border-top:4px solid var(--green);
    background:linear-gradient(180deg,#ffffff 0%,#f1f3f1 55%,#dde3de 100%)}
  .footer-brand{position:absolute;left:0;width:1200px;top:28px;display:flex;justify-content:center;align-items:center;gap:8px;
    font-family:"Poppins",sans-serif;font-weight:600;font-size:14px;letter-spacing:1px;color:var(--ink)}
  .footer-brand .brand-dot{width:24px;height:24px}
  .footer-nav{position:absolute;left:0;width:1200px;top:86px;display:flex;justify-content:center;gap:30px;
    font-family:"Poppins",sans-serif;font-size:11px;color:var(--ink)}
  .footer-nav a{color:inherit;text-decoration:none}
  .social{position:absolute;left:0;width:1200px;top:126px;display:flex;justify-content:center;gap:12px}
  .social span{width:24px;height:24px;border-radius:50%;background:#dfe3e0;border:1px solid #c9cfcb}
  .copyright{position:absolute;left:0;width:1200px;top:176px;text-align:center;font-size:10px;color:var(--muted)}
</style>
</head>
<body>

<section class="hero" role="img" aria-label="Golden wheat field under a soft misty sky"></section>

<header class="site-header">
  <div class="brand"><span class="brand-dot"></span>VELORA</div>
  <nav class="main-nav">
    <a class="active" href="#">Home</a>
    <a href="#">What We Do</a>
    <a href="#">Who We Are</a>
    <a href="#">Success Stories</a>
    <a href="#">What You Can Do</a>
    <a href="#">Donate</a>
    <a href="#">Join</a>
  </nav>
</header>

<h1 class="hero-title"><span class="strong">Help Raise</span><span class="light">World Fibration</span></h1>
<p class="hero-text">We care for the planet, its animals and every life within it. Together we can restore balance and bring lasting calm to the world we share.</p>
<a class="btn btn-solid hero-cta" href="#">Make a difference</a>

<article class="card" style="left:68px">
  <div class="card-media media-forest" role="img" aria-label="Aerial view of a snowy forest road"></div>
  <div class="card-icon">
    <svg width="28" height="28" viewBox="0 0 28 28" fill="none" stroke="#1f8a3f" stroke-width="1.6"><path d="M6 22C6 12 12 6 22 6c0 10-6 16-16 16z"/><path d="M6 22L16 12"/></svg>
  </div>
  <h2 class="card-title">Environment</h2>
  <p class="card-text">Protecting forests, rivers and open land so that every living thing has a healthy home to grow and thrive in.</p>
  <a class="btn btn-outline" href="#">Find out more</a>
</article>

<article class="card" style="left:432px">
  <div class="card-media media-snow" role="img" aria-label="Snow leopard walking through a misty winter forest"></div>
  <div class="card-icon">
    <svg width="28" height="28" viewBox="0 0 28 28" fill="none" stroke="#1f8a3f" stroke-width="1.6"><circle cx="8" cy="11" r="2.5"/><circle cx="13" cy="7" r="2.5"/><circle cx="19" cy="8" r="2.5"/><circle cx="22" cy="13" r="2.5"/><path d="M9 21c0-4 3-7 6-7s5 3 5 6-3 3-5 2-6 2-6-1z"/></svg>
  </div>
  <h2 class="card-title">Animal</h2>
  <p class="card-text">Caring for wild creatures and their habitats, giving endangered species the safe space they need to return.</p>
  <a class="btn btn-outline" href="#">Find out more</a>
</article>

<article class="card" style="left:796px">
  <div class="card-media media-meadow" role="img" aria-label="Person holding a child in a green summer garden"></div>
  <div class="card-icon">
    <svg width="28" height="28" viewBox="0 0 28 28" fill="none" stroke="#1f8a3f" stroke-width="1.6"><circle cx="14" cy="9" r="4"/><path d="M6 24c0-5 4-8 8-8s8 3 8 8"/></svg>
  </div>
  <h2 class="card-title">Human</h2>
  <p class="card-text">Helping people reconnect with nature and each other, building kinder communities for a balanced future.</p>
  <a class="btn btn-outline" href="#">Find out more</a>
</article>

<h2 class="feature-title" style="left:84px;top:1196px">Environment</h2>
<p class="feature-text" style="left:84px;top:1256px">Our environment programmes restore woodland, clean waterways and protect the soil that feeds us. We work with local partners around the world, planting trees, reviving wetlands and teaching communities how to care for the land. Every donation helps us reach another region in need.</p>
<a class="btn btn-outline abs" style="left:84px;top:1414px" href="#">Find out more</a>
<div class="feature-media media-road" style="left:608px;top:1184px;width:508px;height:236px" role="img" aria-label="Aerial view of a road cutting through a snowy pine forest"></div>

<div class="feature-media media-mist" style="left:84px;top:1584px;width:508px;height:276px" role="img" aria-label="Snow leopard in a misty snowy forest"></div>
<h2 class="feature-title" style="left:640px;top:1600px">Animal</h2>
<p class="feature-text" style="left:640px;top:1660px">From snow leopards to songbirds, we support rescue centres, anti-poaching patrols and safe migration routes. Our teams track vulnerable populations, rehabilitate injured animals and return them to the wild whenever possible. Your support keeps these vital projects running all year round.</p>
<a class="btn btn-outline abs" style="left:640px;top:1818px" href="#">Find out more</a>

<footer class="site-footer">
  <div class="footer-brand"><span class="brand-dot"></span>VELORA</div>
  <nav class="footer-nav">
    <a href="#">Home</a>
    <a href="#">What We Do</a>
    <a href="#">Who We Are</a>
    <a href="#">Success Stories</a>
    <a href="#">What You Can Do</a>
    <a href="#">Donate</a>
    <a href="#">Join</a>
  </nav>
  <div class="social"><span></span><span></span><span></span></div>
  <p class="copyright">© 2024 Velora. All rights reserved.</p>
</footer>

</body>
</html>
```